Consulting company needs Business Cards - rough concept provided

I'm looking for someone to take our business card idea and make is slick and polished - to communicate our high-end, sophisticated, serious consulting business. We have a rough layout we did in-house. We are open to ideas on repo-ing elements, adjusting sizes, typefaces etc... within the general concept we've already come up with. We want it to be super-clean and sophisticated. We want to keep the white backgrounds, and blue brand colors. Our goal is to print with painted blue edges on thick cardstock. Thank you!!

```html
<!DOCTYPE html>
<html lang="en">
<head>
<meta charset="utf-8">
<title>Tallmere Stationery</title>
<link href="https://fonts.googleapis.com/css2?family=Source+Sans+3:wght@400;600;700&display=swap" rel="stylesheet">
<style>
:root{
  --bg:#ecebe8;
  --paper:#f6f6f4;
  --blue:#0a64c8;
  --blue-deep:#0a5bbd;
  --ink:#1d1d1f;
  --muted:#55575c;
  --rule:#c9c9c9;
  --emboss:#e3e3e1;
}
*{margin:0;padding:0;box-sizing:border-box}
html,body{width:1200px;height:960px;overflow:hidden;background:var(--bg);font-family:"Source Sans 3",Arial,sans-serif;color:var(--ink)}
.canvas{position:relative;width:1200px;height:960px}
.sheet{position:absolute;background:var(--paper);box-shadow:0 2px 6px rgba(0,0,0,.12)}
.brand{font-weight:700;color:var(--blue);letter-spacing:-.5px;line-height:1}
.caps{text-transform:uppercase;letter-spacing:.6px}

/* letterhead */
.backing{position:absolute;left:54px;top:162px;width:498px;height:695px;background:var(--blue)}
.letter{left:83px;top:90px;width:527px;height:732px}
.letter .brand{position:absolute;left:34px;top:50px;font-size:44px}
.tagline{position:absolute;left:418px;top:52px;font-size:7.5px;font-weight:700;line-height:10px;letter-spacing:.8px}
.vrule{position:absolute;left:418px;top:113px;width:1px;height:294px;background:var(--rule)}
.sender{position:absolute;left:34px;top:158px;font-size:7px;line-height:10px;color:var(--blue)}
.sender .web{margin-top:9px;font-weight:700}
.recipient{position:absolute;left:34px;top:255px;font-size:7px;line-height:12.3px}
.recipient b{font-weight:700}
.date{position:absolute;left:34px;top:332px;font-size:7px}
.body{position:absolute;left:34px;top:376px;width:238px;font-size:7px;line-height:12.3px}
.body p{margin-bottom:13px}
.signature{width:92px;height:26px;margin:-4px 0 8px;background:linear-gradient(90deg,#dfe7f3,#c7d6ee)}
.signer{font-size:7px;line-height:12.3px}
.drawing{position:absolute;left:272px;top:368px;width:255px;height:261px;background:linear-gradient(160deg,rgba(246,246,244,0) 0%,#e6e6e4 55%,#dcdcda 100%)}
.foot-rule{position:absolute;left:34px;top:659px;width:447px;height:1px;background:var(--rule)}
.foot-rule::before{content:"";position:absolute;left:0;top:-1px;width:49px;height:2px;background:var(--blue)}
.services{position:absolute;left:49px;top:687px;display:flex;gap:12px;font-size:7.5px;letter-spacing:.7px}
.services span.dot{font-size:8px}
.foot-mark{position:absolute;left:477px;top:682px;width:13px;height:13px;background:var(--blue-deep)}

/* envelope front */
.env-front{left:644px;top:161px;width:503px;height:252px}
.env-front .brand{position:absolute;left:22px;top:30px;font-size:28px}
.cross{position:absolute}
.env-front .cross{left:434px;top:20px}
.env-sender{position:absolute;left:22px;top:182px;font-size:7px;line-height:10.5px;color:var(--blue)}
.env-to{position:absolute;left:298px;top:129px;padding-left:20px;border-left:1.5px solid var(--blue);font-size:9.5px;line-height:14.5px;letter-spacing:.7px}
.env-to b{font-weight:700}

/* envelope back */
.env-back{left:644px;top:447px;width:503px;height:233px;overflow:hidden}
.env-back svg.flap{position:absolute;left:0;top:0}
.env-back .brand{position:absolute;left:0;width:503px;top:40px;text-align:center;font-size:21px;color:#fff}
.env-back .cross{left:243px;top:144px}
.env-addr{position:absolute;left:0;width:503px;top:182px;text-align:center;font-size:7px;letter-spacing:.6px;color:var(--muted);word-spacing:3px}
.env-web{position:absolute;left:0;width:503px;top:201px;text-align:center;font-size:7px;letter-spacing:.6px;color:var(--blue)}

/* business cards */
.card{width:238px;height:145px;border-left:3px solid var(--blue);border-bottom:4px solid var(--blue)}
.card-front{left:641px;top:721px}
.card-back{left:905px;top:721px}
.card-front .brand{position:absolute;left:20px;top:20px;font-size:23px}
.card-name{position:absolute;left:20px;top:100px;font-size:6.5px;line-height:12px;letter-spacing:.5px}
.card-name b{color:var(--blue);font-weight:700}
.card-divider{position:absolute;left:100px;top:92px;width:1px;height:32px;background:var(--blue)}
.card-contact{position:absolute;left:112px;top:90px;font-size:6px;line-height:12px;letter-spacing:.3px}
.card-back .brand{position:absolute;left:0;width:235px;top:62px;text-align:center;font-size:20px;color:var(--emboss);text-shadow:0 1px 0 #fff}
.card-back .cross{left:190px;top:65px}
</style>
</head>
<body>
<div class="canvas">

  <div class="backing"></div>
  <section class="sheet letter">
    <div class="brand">TALLMERE</div>
    <div class="tagline caps">Strategy.<br>Transformation.<br>Growth.</div>
    <div class="vrule"></div>
    <address class="sender caps" style="font-style:normal">
      84 Harbor Row<br>Suite 500<br>New York, NY 10001<br>USA
      <div class="web">tallmere.com</div>
    </address>
    <div class="recipient caps">
      <b>Peter Hollis</b><br>Managing Partner<br>Hollis Partners<br>12 Linden Court<br>New York, NY 10001
    </div>
    <div class="date caps">May 20, 2025</div>
    <div class="body">
      <p>Dear Peter,</p>
      <p>Lorem ipsum dolor sit amet, consectetur adipiscing elit, sed do eiusmod tempor incididunt ut labore et dolore magna aliqua. Ut enim ad minim veniam, quis nostrud exercitation ullamco laboris nisi ut aliquip ex ea commodo consequat.</p>
      <p>Duis aute irure dolor in reprehenderit in voluptate velit esse cillum dolore eu fugiat nulla pariatur. Excepteur sint occaecat cupidatat non proident, sunt in culpa qui officia deserunt mollit anim id est laborum.</p>
      <p>Sincerely,</p>
      <div class="signature" role="img" aria-label="Handwritten signature"></div>
      <div class="signer caps"><b>Clara Whitfield</b><br>Managing Partner</div>
    </div>
    <div class="drawing" role="img" aria-label="Faint architectural line drawing of arcs and construction lines"></div>
    <div class="foot-rule"></div>
    <div class="services caps">
      <span>Advisory</span><span class="dot">•</span><span>Strategy</span><span class="dot">•</span><span>Operations</span><span class="dot">•</span><span>Transformation</span>
    </div>
    <div class="foot-mark"></div>
  </section>

  <section class="sheet env-front">
    <div class="brand">TALLMERE</div>
    <svg class="cross" width="56" height="36" viewBox="0 0 56 36"><path d="M0 16H56M12 0V34" stroke="#c4c4c4" stroke-width="1" fill="none"/></svg>
    <div class="env-sender caps">84 Harbor Row<br>Suite 500<br>New York, NY 10001<br>USA</div>
    <div class="env-to caps"><b>Peter Hollis</b><br>Hollis Partners<br>12 Linden Court<br>New York, NY 10001</div>
  </section>

  <section class="sheet env-back">
    <svg width="503" height="233" viewBox="0 0 503 233" style="position:absolute;left:0;top:0">
      <path d="M0 90L110 150M503 90L393 150M0 233L140 140M503 233L363 140" stroke="#dedede" stroke-width="1" fill="none"/>
    </svg>
    <svg class="flap" width="503" height="92" viewBox="0 0 503 92">
      <path d="M0 0H503L468 80Q463 91 445 91H58Q40 91 35 80Z" fill="var(--blue)"/>
    </svg>
    <div class="brand">TALLMERE</div>
    <svg class="cross" width="16" height="16" viewBox="0 0 16 16"><path d="M0 8H16M8 0V16" stroke="var(--blue)" stroke-width="1"/></svg>
    <div class="env-addr caps">84 Harbor Row &nbsp; Suite 500 &nbsp; New York, NY 10001 &nbsp; USA</div>
    <div class="env-web caps">tallmere.com</div>
  </section>

  <section class="sheet card card-front">
    <div class="brand">TALLMERE</div>
    <div class="card-name caps"><b>Clara Whitfield</b><br>Managing Partner</div>
    <div class="card-divider"></div>
    <div class="card-contact caps">+1 212 555 0187<br>clara.whitfield@tallmere.com<br>tallmere.com</div>
  </section>

  <section class="sheet card card-back">
    <div class="brand">TALLMERE</div>
    <svg class="cross" width="14" height="14" viewBox="0 0 14 14" style="top:68px"><path d="M0 7H14M7 0V14" stroke="var(--blue)" stroke-width="1"/></svg>
  </section>

</div>
</body>
</html>
```